website design for online company - registration of companies AUSTRALIA

website name: velmora482.com.au
purpose of the website: register NEW australian companies

once a client submits their order, our website will submit information to a government agency and in under 20 minutes, the client will receive their new company together with legal documentation:

key features:
- simplicity
- ease of use
- clarity
- fast
- competitive
- trust

our competitors:
www.quickdratel.com.au
www.zentrafirms.com.au

the website needs to be dynamic, clear and portray simplicity as the name suggests.

"register your company online with OREV in 3 simple steps"
1 fill in a short form
2 submit payment
3 receive your company

headings - similar to our competitors but needs to be different.

Design only no coding

if you have any questions, feel free to ask

people in business

Government

Serif

• simple
creative
elegant
• top graphics

```html
<!DOCTYPE html>
<html lang="en">
<head>
<meta charset="utf-8">
<title>Velmora482 – Australian Company Registration</title>
<link rel="stylesheet" href="https://fonts.googleapis.com/css2?family=Roboto+Condensed:wght@400;700&family=Arimo:wght@400;700&display=swap">
<style>
:root{
  --teal:#1fa58a;
  --teal-dark:#178f77;
  --teal-light:#46c9a6;
  --navy:#2a3a4e;
  --navy-band:#2c3a4f;
  --orange:#f5b921;
  --card:#e8e8e8;
  --card-text:#666;
  --footer:#4a4f5e;
  --footer-bottom:#3a3e4a;
  --white:#fff;
  --text:#333;
}
*{box-sizing:border-box;margin:0;padding:0}
html,body{width:1200px;height:947px;overflow:hidden;background:var(--white)}
body{font-family:"Arimo",Arial,sans-serif;color:var(--text)}
.page{position:relative;width:1200px;height:947px;overflow:hidden}
.abs{position:absolute}

/* header */
.site-header{left:0;top:0;width:1200px;height:66px;background:var(--white)}
.brand{left:267px;top:16px;display:flex;align-items:center;gap:8px;font-family:"Roboto Condensed",sans-serif;font-weight:700;font-size:30px;color:var(--navy);letter-spacing:-.5px}
.brand-dot{width:14px;height:14px;border-radius:50%;background:var(--teal)}
.btn-head{top:19px;height:27px;width:83px;border-radius:3px;font-size:11px;display:flex;align-items:center;justify-content:center;color:var(--navy)}
.btn-signup{left:765px;background:linear-gradient(#3fd0ae,#1fa58a);border:1px solid #189a80}
.btn-login{left:854px;background:linear-gradient(#ffd04a,#f0a91a);border:1px solid #dc9a12}

/* nav */
.main-nav{left:0;top:66px;width:1200px;height:27px;background:var(--teal)}
.main-nav ul{list-style:none;display:flex;position:absolute;left:258px;top:0;height:27px}
.main-nav li{font-size:12px;color:var(--white);padding:0 13px;line-height:27px}
.main-nav li.active{background:var(--teal-light);padding:0 17px}

/* hero */
.hero{left:0;top:93px;width:1200px;height:223px;background:linear-gradient(120deg,#23a88a 0%,#38be9c 50%,#2cb092 100%)}
.hero-title{left:278px;top:22px;font-family:"Roboto Condensed",sans-serif;color:var(--white);font-size:27px;line-height:1.2}
.hero-title .line2{font-size:24px;display:block;margin-top:4px}
.hero-title .price{font-size:33px;color:var(--navy)}
.hero-sub{left:278px;top:99px;width:380px;font-family:"Roboto Condensed",sans-serif;color:var(--white);font-size:15px;line-height:20px}
.btn-start{left:278px;top:151px;width:118px;height:33px;border-radius:4px;background:linear-gradient(#fff,#d8d8d8);border:1px solid #bbb;font-family:"Roboto Condensed",sans-serif;font-weight:700;font-size:19px;color:var(--navy);display:flex;align-items:center;justify-content:center}
.hero-art{left:660px;top:10px;width:230px;height:213px;background:radial-gradient(ellipse at 50% 45%,#c9d3dc 0%,#8a9aaa 55%,rgba(60,80,100,.0) 75%)}

/* name check */
.name-check{left:0;top:316px;width:1200px;height:46px;background:linear-gradient(#34455b,#25334a)}
.name-check .label{left:275px;top:14px;font-size:14px;color:var(--white)}
.name-input{left:495px;top:11px;width:328px;height:25px;background:var(--white);border:1px solid #ccc;font-size:11px;color:#777;padding-left:9px;line-height:23px}
.name-btn{left:823px;top:11px;width:100px;height:25px;background:var(--teal);color:var(--white);font-size:11px;text-align:center;line-height:25px}

/* steps */
.steps-title{left:0;top:382px;width:1200px;text-align:center;font-family:"Arimo",sans-serif;font-weight:700;font-size:21px;color:var(--navy)}
.steps{left:0;top:410px;width:1200px;height:110px}
.step-label{top:86px;font-weight:700;font-size:14px;color:var(--teal);text-align:center;width:200px}

/* features */
.feature{width:217px;height:108px;background:var(--card);border-radius:3px}
.feature-icon{left:16px;top:16px;width:32px;height:32px}
.feature h3{position:absolute;left:55px;top:20px;font-size:15px;font-weight:700;color:#444}
.feature p{position:absolute;left:55px;top:44px;width:152px;font-size:8.5px;line-height:13.5px;color:var(--card-text)}

/* footer */
.site-footer{left:0;top:790px;width:1200px;height:124px;background:var(--footer)}
.foot-col{top:17px}
.foot-col h4{font-size:12px;font-weight:400;color:var(--white);padding-bottom:5px;border-bottom:1px solid #6b7080;width:95px;position:relative}
.foot-col h4::after{content:"";position:absolute;left:0;bottom:-1px;width:48px;height:1px;background:var(--teal)}
.foot-col ul{list-style:none;margin-top:12px}
.foot-col li{font-size:8.5px;color:#dcdde2;line-height:15.5px;padding-left:12px;position:relative}
.foot-col li::before{content:"»";position:absolute;left:0;color:var(--teal)}
.follow p{font-size:8.5px;color:#dcdde2;line-height:12.5px;width:115px;margin-top:12px}
.social{display:flex;gap:6px;margin-top:8px}
.social span{width:22px;height:22px;border-radius:50%;background:#6c7080}
.social span.on{background:var(--teal)}
.copyright{left:0;top:914px;width:1200px;height:33px;background:var(--footer-bottom);color:var(--white);font-size:10px;text-align:center;line-height:33px}
</style>
</head>
<body>
<div class="page">

  <header class="site-header abs">
    <div class="brand abs"><span>VELMORA482</span><span class="brand-dot"></span></div>
    <div class="btn-head btn-signup abs">SIGN UP</div>
    <div class="btn-head btn-login abs">LOG IN</div>
  </header>

  <nav class="main-nav abs">
    <ul>
      <li class="active">Home</li>
      <li>Register a Company</li>
      <li>How It Works</li>
      <li>Online Application</li>
      <li>Why Use Us</li>
      <li>FAQs</li>
      <li>Client Area</li>
    </ul>
  </nav>

  <section class="hero abs">
    <h1 class="hero-title abs" style="font-weight:400">Australian Company Registration<span class="line2">in 20 Minutes for <span class="price">$469</span></span></h1>
    <p class="hero-sub abs">Fast, simple, trusted. Completely online for just $494 ABN, GST and PAYG registration only $50 extra</p>
    <div class="btn-start abs">START NOW</div>
    <div class="hero-art abs" role="img" aria-label="Illustration of a modern office building"></div>
  </section>

  <section class="name-check abs">
    <span class="label abs">Is your company name available?</span>
    <div class="name-input abs">Check your company Name</div>
    <div class="name-btn abs">Check Availability</div>
  </section>

  <h2 class="steps-title abs">REGISTER A COMPANY ONLINE WITH OREV IN 3 SIMPLE STEPS</h2>
  <section class="steps abs">
    <svg width="1200" height="80" viewBox="0 0 1200 80">
      <line x1="286" y1="58" x2="905" y2="58" stroke="#1a8f78" stroke-width="4"/>
      <line x1="595" y1="4" x2="595" y2="34" stroke="#1a8f78" stroke-width="4"/>
      <circle cx="286" cy="58" r="7" fill="#1a8f78"/>
      <circle cx="905" cy="58" r="7" fill="#1a8f78"/>
      <g fill="#1fa58a" stroke="#fff" stroke-width="3">
        <circle cx="369" cy="58" r="26"/><circle cx="595" cy="58" r="26"/><circle cx="816" cy="58" r="26"/>
      </g>
      <g fill="none" stroke="#fff" stroke-width="2" stroke-linejoin="round">
        <rect x="358" y="47" width="20" height="22"/><path d="M362 56h10M362 61h8M370 63l12-14 3 3-12 14-4 1z"/>
        <rect x="582" y="49" width="26" height="16" transform="rotate(-15 595 57)"/><circle cx="595" cy="57" r="4"/>
        <path d="M803 58v10h26V58M803 58l6-8h14l6 8h-8a5 5 0 0 1-10 0z"/><path d="M816 44v10m-4-4 4 4 4-4"/>
      </g>
    </svg>
    <div class="step-label abs" style="left:269px">1 Fill in a Short Form</div>
    <div class="step-label abs" style="left:495px;top:88px">2 Submit Payment</div>
    <div class="step-label abs" style="left:716px">3 Receive Your Company</div>
  </section>

  <section class="features">
    <article class="feature abs" style="left:260px;top:540px">
      <svg class="feature-icon abs" viewBox="0 0 32 32"><circle cx="16" cy="16" r="16" fill="#3b4457"/><circle cx="16" cy="16" r="8" fill="none" stroke="#fff" stroke-width="2"/></svg>
      <h3>Simplicity</h3>
      <p>Lorem Ipsum is simply dummy text of the printing and typesetting industry. Lorem Ipsum has been the industry's standard unknown printer.</p>
    </article>
    <article class="feature abs" style="left:489px;top:540px">
      <svg class="feature-icon abs" viewBox="0 0 32 32"><circle cx="16" cy="16" r="16" fill="#3b4457"/><path d="M10 17l4 4 8-10" fill="none" stroke="#fff" stroke-width="2.5"/></svg>
      <h3>Ease of Use</h3>
      <p>Lorem Ipsum is simply dummy text of the printing and typesetting industry. Lorem Ipsum has been the industry's standard unknown printer.</p>
    </article>
    <article class="feature abs" style="left:718px;top:540px">
      <svg class="feature-icon abs" viewBox="0 0 32 32"><circle cx="16" cy="16" r="16" fill="#3b4457"/><circle cx="16" cy="15" r="7" fill="#fff"/><rect x="13" y="21" width="6" height="4" fill="#fff"/></svg>
      <h3>Clarity</h3>
      <p>Lorem Ipsum is simply dummy text of the printing and typesetting industry. Lorem Ipsum has been the industry's standard unknown printer.</p>
    </article>
    <article class="feature abs" style="left:260px;top:661px">
      <svg class="feature-icon abs" viewBox="0 0 32 32"><circle cx="16" cy="16" r="16" fill="#3b4457"/><path d="M18 7l-8 11h6l-2 8 8-11h-6z" fill="#fff"/></svg>
      <h3>Fast</h3>
      <p>Lorem Ipsum is simply dummy text of the printing and typesetting industry. Lorem Ipsum has been the industry's standard unknown printer.</p>
    </article>
    <article class="feature abs" style="left:489px;top:661px">
      <svg class="feature-icon abs" viewBox="0 0 32 32"><circle cx="16" cy="16" r="16" fill="#3b4457"/><g fill="#fff"><circle cx="10" cy="14" r="2.5"/><circle cx="16" cy="12" r="2.5"/><circle cx="22" cy="14" r="2.5"/><rect x="8" y="18" width="4" height="7"/><rect x="14" y="16" width="4" height="9"/><rect x="20" y="18" width="4" height="7"/></g></svg>
      <h3>Competitive</h3>
      <p>Lorem Ipsum is simply dummy text of the printing and typesetting industry. Lorem Ipsum has been the industry's standard unknown printer.</p>
    </article>
    <article class="feature abs" style="left:718px;top:661px">
      <svg class="feature-icon abs" viewBox="0 0 32 32"><circle cx="16" cy="16" r="16" fill="#3b4457"/><path d="M7 15l5-4 4 2 4-2 5 4-7 6h-4z" fill="#fff"/></svg>
      <h3>Trust</h3>
      <p>Lorem Ipsum is simply dummy text of the printing and typesetting industry. Lorem Ipsum has been the industry's standard unknown printer.</p>
    </article>
  </section>

  <footer class="site-footer abs">
    <div class="foot-col abs" style="left:279px"><h4>Our Services</h4>
      <ul><li>Register a company</li><li>Domain Registration</li><li>ABN Registration</li><li>Document Printing</li></ul></div>
    <div class="foot-col abs" style="left:422px"><h4>Support</h4>
      <ul><li>Contact Us</li><li>Resources</li><li>FAQs</li><li>Glossary</li></ul></div>
    <div class="foot-col abs" style="left:541px"><h4>Legals</h4>
      <ul><li>Privacy Statement</li><li>Terms &amp; Conditions</li><li>About Us</li></ul></div>
    <div class="foot-col abs" style="left:669px"><h4>More Information</h4>
      <ul><li>Sitemap</li><li>Blog</li><li>Partners</li><li>Testimonials</li></ul></div>
    <div class="foot-col follow abs" style="left:817px"><h4>Follow Us</h4>
      <p>Keep up to date with our latest offerings and products.</p>
      <div class="social"><span class="on"></span><span></span><span></span></div></div>
  </footer>
  <div class="copyright abs">Copyright © 2014 Velmora482. All rights reserved.</div>

</div>
</body>
</html>
```